Cardiology practice business card

We need a business card for our cardiology practice "Bellmoor Cardiology". We have a new logo, attached below. We like the colours in the logo - red and charcoal. The front of the business card will need to have the doctors name, address, phone number and email. The back will need to have space to write 2 appointment dates and times.

```html
<!DOCTYPE html>
<html lang="en">
<head>
<meta charset="utf-8">
<title>Bellmoor Cardiology – Business Card</title>
<link href="https://fonts.googleapis.com/css2?family=Montserrat:wght@500;600;700&display=swap" rel="stylesheet">
<style>
  :root {
    --backdrop: #d6d4d5;
    --card: #ffffff;
    --red: #e0101a;
    --charcoal: #6d6e71;
    --rule: #8a8a8c;
  }
  html, body {
    margin: 0;
    width: 1200px;
    height: 1109px;
    overflow: hidden;
    background: var(--backdrop);
    font-family: "Montserrat", sans-serif;
  }
  .card {
    position: absolute;
    left: 216px;
    width: 768px;
    height: 439px;
    background: var(--card);
    overflow: hidden;
  }
  .card--front { top: 71px; }
  .card--back { top: 570px; }
  .card__waves {
    position: absolute;
    inset: 0;
    width: 100%;
    height: 100%;
  }
  .card__waves path { fill: var(--red); }

  .brand {
    position: absolute;
    display: flex;
    align-items: center;
    gap: 12px;
    color: var(--red);
    font-weight: 700;
    text-transform: uppercase;
    letter-spacing: 1px;
    line-height: 1.05;
    white-space: nowrap;
  }
  .brand__dot {
    width: 18px;
    height: 18px;
    border-radius: 50%;
    background: var(--red);
    flex: none;
  }
  .card--front .brand {
    left: 0; right: 0;
    top: 170px;
    justify-content: center;
    font-size: 34px;
  }
  .card--back .brand {
    left: 96px;
    top: 178px;
    font-size: 30px;
  }

  .appointments {
    position: absolute;
    left: 214px;
    top: 262px;
    width: 340px;
    color: var(--charcoal);
  }
  .appointments__title {
    margin: 0 0 14px;
    font-size: 13px;
    font-weight: 600;
    letter-spacing: 2.5px;
    color: var(--red);
    text-align: center;
  }
  .appointments__slot {
    display: flex;
    align-items: flex-end;
    gap: 8px;
    margin-bottom: 16px;
    font-size: 13px;
    font-weight: 600;
    letter-spacing: 0.5px;
  }
  .appointments__field {
    flex: 1;
    border-bottom: 1.5px solid var(--rule);
    height: 16px;
  }
  .appointments__field--time { flex: 0 0 90px; }

  .divider {
    position: absolute;
    left: 383px;
    top: 85px;
    width: 2px;
    height: 280px;
    background: var(--rule);
  }
  .person {
    position: absolute;
    left: 416px;
    top: 92px;
  }
  .person__name {
    margin: 0;
    font-size: 47px;
    font-weight: 600;
    color: var(--charcoal);
    letter-spacing: -1.5px;
    line-height: 1;
  }
  .person__role {
    margin: 6px 0 0;
    font-size: 17px;
    font-weight: 600;
    color: var(--red);
    letter-spacing: 2.5px;
  }
  .person__rule {
    width: 180px;
    height: 2px;
    background: var(--rule);
    margin-top: 14px;
  }
  .contacts {
    position: absolute;
    left: 422px;
    top: 200px;
    margin: 0;
    padding: 0;
    list-style: none;
  }
  .contacts li {
    display: flex;
    align-items: center;
    height: 28px;
    margin-bottom: 18px;
    font-size: 17px;
    font-weight: 600;
    color: var(--charcoal);
    letter-spacing: 0.8px;
    white-space: nowrap;
  }
  .contacts svg {
    width: 26px;
    height: 26px;
    margin-right: 25px;
    flex: none;
  }
</style>
</head>
<body>

<section class="card card--front">
  <svg class="card__waves" viewBox="0 0 1280 732" preserveAspectRatio="none" aria-hidden="true">
    <path d="M880,0 C1100,0 1280,180 1280,401 V0 Z"/>
    <path d="M0,351 C0,560 180,732 400,732 H0 Z"/>
  </svg>
  <div class="brand"><span class="brand__dot"></span>Bellmoor Cardiology</div>

  <div class="appointments">
    <p class="appointments__title">NEXT APPOINTMENTS</p>
    <div class="appointments__slot">Date <span class="appointments__field"></span> Time <span class="appointments__field appointments__field--time"></span></div>
    <div class="appointments__slot">Date <span class="appointments__field"></span> Time <span class="appointments__field appointments__field--time"></span></div>
  </div>
</section>

<section class="card card--back">
  <svg class="card__waves" viewBox="0 0 1280 732" preserveAspectRatio="none" aria-hidden="true">
    <path d="M880,0 C1100,0 1280,180 1280,401 V0 Z"/>
    <path d="M0,351 C0,560 180,732 400,732 H0 Z"/>
  </svg>

  <div class="brand"><span class="brand__dot"></span>Bellmoor<br>Cardiology</div>

  <div class="divider"></div>

  <div class="person">
    <h1 class="person__name">Dr Whitford</h1>
    <p class="person__role">DESIGNATION</p>
    <div class="person__rule"></div>
  </div>

  <ul class="contacts">
    <li>
      <svg viewBox="0 0 26 26" aria-hidden="true">
        <circle cx="13" cy="13" r="13" fill="#e0101a"/>
        <path d="M9.2 7.5l2 2.4-1.2 1.5c.8 1.7 2 2.9 3.6 3.7l1.5-1.2 2.4 2-1.2 1.8c-4.3-.4-8.1-4.2-8.6-8.6z" fill="#fff"/>
      </svg>
      +070 5521 39087
    </li>
    <li>
      <svg viewBox="0 0 26 26" aria-hidden="true">
        <circle cx="13" cy="13" r="13" fill="#e0101a"/>
        <rect x="7" y="9" width="12" height="8.5" fill="none" stroke="#fff" stroke-width="1.4"/>
        <path d="M7 9l6 5 6-5M7 17.5l4.3-4M19 17.5l-4.3-4" fill="none" stroke="#fff" stroke-width="1.2"/>
      </svg>
      bellmoor@heartmail.com
    </li>
    <li>
      <svg viewBox="0 0 26 26" aria-hidden="true">
        <circle cx="13" cy="13" r="13" fill="#e0101a"/>
        <g fill="none" stroke="#fff" stroke-width="1.3">
          <circle cx="13" cy="13" r="7"/>
          <ellipse cx="13" cy="13" rx="3" ry="7"/>
          <path d="M6 13h14M7 9.5h12M7 16.5h12"/>
        </g>
      </svg>
      www.bellmoorheart.com
    </li>
    <li>
      <svg viewBox="0 0 26 26" aria-hidden="true">
        <circle cx="13" cy="13" r="13" fill="#e0101a"/>
        <path d="M13 6.5c-2.8 0-5 2.1-5 4.8 0 3.6 5 8.2 5 8.2s5-4.6 5-8.2c0-2.7-2.2-4.8-5-4.8z" fill="#fff"/>
        <circle cx="13" cy="11.3" r="1.8" fill="#e0101a"/>
      </svg>
      12 Harbour Lane, Bellmoor
    </li>
  </ul>
</section>

</body>
</html>
```